Web Design Project - Old Brackley (Bar)

We need a website for a new wine bar/hotel opening in Sydney's Kings Cross area. The concept is a rustic Australiana bar. We intend to use raw materials (sandstone, rusty metal etc) and lots of greenery/plants. It is set to be stylish and accessible to a young and middle age clientele.

The idea is to bring the outside inside.

The venue can cater for 450 people and is in one of the major nightclub strips in Australia. The demographic differs from celebrities to backpackers.

Target Market(s)

We are targeting 23yr - 40yr olds.

Industry/Entity Type

Hotel

Requirements
Must have
• What I want is a design to reflect is the fit out of the bar. We would like to see a rustic design to reflect the theme of the bar. The theme behind the fit out will be "bringing the outside inside" with lots of plants, wet walls etc.. There will be exposed brickwork, sandstone, timber and rusted steel with laser cut designs throughout the venue.
Nice to have
• I've attached some 3D designs that the venue will be roughly based on.

```html
<!DOCTYPE html>
<html lang="en">
<head>
<meta charset="utf-8">
<title>Old Brackley</title>
<link href="https://fonts.googleapis.com/css2?family=Federo&family=Arimo:wght@400;700&display=swap" rel="stylesheet">
<style>
:root{
  --bar:#141210;
  --bar-line:#3a3632;
  --band:rgba(10,10,10,.45);
  --text:#f2f2f2;
  --muted:#b5b0aa;
  --accent:#e8d640;
  --arrow:#c9c22a;
  --nav-mark:#7fae3a;
  --field:#2b2724;
  --field-line:#5a5550;
  --logo-bg:#6e5534;
  --logo-ink:#1c140c;
  --frame:#cfcfcf;
}
*{box-sizing:border-box;margin:0;padding:0}
html,body{width:1200px;height:900px;overflow:hidden;background:#111}
body{position:relative;font-family:"Arimo",Arial,sans-serif;color:var(--text)}
.scene{position:absolute;inset:0;background:
  radial-gradient(ellipse at 85% 30%,rgba(70,90,50,.55),transparent 55%),
  radial-gradient(ellipse at 20% 60%,rgba(60,55,50,.6),transparent 60%),
  linear-gradient(180deg,#2c2a27 0%,#242220 45%,#1d1b19 100%)}
.band{position:absolute;left:0;right:0;top:205px;height:595px;background:var(--band)}
.topbar{position:absolute;left:0;top:0;width:1200px;height:46px;background:var(--bar);border-bottom:1px solid var(--bar-line)}
.topnav a{position:absolute;top:15px;font-size:14px;color:var(--muted);text-decoration:none}
.topnav a.current{color:var(--text)}
.topnav .marker{position:absolute;left:161px;top:34px}
.search-field{position:absolute;left:770px;top:14px;width:201px;height:20px;background:var(--field);border:1px solid var(--field-line)}
.search-btn{position:absolute;left:979px;top:14px;width:73px;height:21px;background:var(--field);border:1px solid var(--field-line);color:var(--muted);font:13px "Arimo",Arial,sans-serif;text-align:center;line-height:19px}
.brand{position:absolute;left:148px;top:67px;width:211px;height:124px;background:var(--logo-bg);display:flex;align-items:center;justify-content:center;font-family:"Federo",sans-serif;font-size:24px;color:var(--logo-ink);letter-spacing:1px}
h2{position:absolute;font-family:"Federo",sans-serif;font-weight:400;font-size:22px;color:var(--text)}
.photo{position:absolute;width:254px;height:148px;border:2px solid var(--frame)}
.photo.wine{left:171px;top:280px;background:linear-gradient(135deg,#4a3524,#7a5a34 50%,#3a2a1c)}
.photo.bottles{left:526px;top:280px;background:linear-gradient(120deg,#2a1a10,#8a5a18 45%,#c8901c 60%,#3a1a10)}
.blurb{position:absolute;width:303px;font-size:12px;line-height:19px;text-align:justify}
.more{position:absolute;width:79px;height:22px;background:#080808;color:var(--text);font-size:9px;text-align:center;line-height:22px;letter-spacing:.4px}
.menu-list{position:absolute;left:886px;top:274px;list-style:none}
.menu-list li{height:29.8px;font-size:12.5px;display:flex;align-items:center}
.menu-list svg{margin-right:20px}
.about-text{position:absolute;left:146px;top:653px;width:695px;font-size:12px;line-height:19px;text-align:justify}
.contact{position:absolute;left:918px;top:651px;font-size:11px;line-height:23.5px}
.footer{position:absolute;left:0;top:800px;width:1200px;height:100px;border-top:1px solid #5a5652;background:rgba(10,10,10,.35)}
.footnav{position:absolute;top:26px;left:0;width:1200px;font-size:14px}
.footnav a{position:absolute;color:var(--text);text-decoration:none}
.copy{position:absolute;top:66px;left:0;width:1198px;text-align:center;font-size:10px}
</style>
</head>
<body>
<div class="scene" role="img" aria-label="Blurred courtyard of the bar with tables, chairs and green plants"></div>
<div class="band"></div>

<header class="topbar">
  <nav class="topnav">
    <a class="current" style="left:148px">Home</a>
    <a style="left:219px">About Us</a>
    <a style="left:309px">Menu</a>
    <a style="left:377px">Events</a>
    <a style="left:453px">Contact Us</a>
    <svg class="marker" width="10" height="7" viewBox="0 0 10 7"><path d="M0 7 L5 0 L10 7Z" fill="var(--nav-mark)"/></svg>
  </nav>
  <div class="search-field"></div>
  <div class="search-btn">Search</div>
</header>

<div class="brand">OLD BRACKLEY</div>

<h2 style="left:146px;top:226px">Lorem Ipsum</h2>
<div class="photo wine" role="img" aria-label="Wine bottles, glasses, grapes and cheese on a table"></div>
<p class="blurb" style="left:148px;top:458px">Lorem Ipsum is simply dummy text of the printing and typesetting industry. Lorem Ipsum has been the industry's standard dummy text ever since the 1500s, when an unknown printer took a galley</p>
<div class="more" style="left:371px;top:548px">Read More...</div>

<h2 style="left:502px;top:226px">Lorem Ipsum is simply</h2>
<div class="photo bottles" role="img" aria-label="Close-up of wine bottles lying in a rack"></div>
<p class="blurb" style="left:504px;top:458px">Lorem Ipsum is simply dummy text of the printing and typesetting industry. Lorem Ipsum has been the industry's standard dummy text ever since the 1500s, when an unknown printer took a galley</p>
<div class="more" style="left:727px;top:548px">Read More...</div>

<h2 style="left:861px;top:226px">Our Menu</h2>
<ul class="menu-list">
  <li><svg width="6" height="9"><path d="M0 0L6 4.5L0 9Z" fill="var(--arrow)"/></svg>Appetizer</li>
  <li><svg width="6" height="9"><path d="M0 0L6 4.5L0 9Z" fill="var(--arrow)"/></svg>Soups</li>
  <li><svg width="6" height="9"><path d="M0 0L6 4.5L0 9Z" fill="var(--arrow)"/></svg>Salads</li>
  <li><svg width="6" height="9"><path d="M0 0L6 4.5L0 9Z" fill="var(--arrow)"/></svg>Main Course (Curries)</li>
  <li><svg width="6" height="9"><path d="M0 0L6 4.5L0 9Z" fill="var(--arrow)"/></svg>Tandoori Specials</li>
  <li><svg width="6" height="9"><path d="M0 0L6 4.5L0 9Z" fill="var(--arrow)"/></svg>Freshly Baked Breads</li>
  <li><svg width="6" height="9"><path d="M0 0L6 4.5L0 9Z" fill="var(--arrow)"/></svg>Australian Specials</li>
  <li><svg width="6" height="9"><path d="M0 0L6 4.5L0 9Z" fill="var(--arrow)"/></svg>Desserts</li>
  <li><svg width="6" height="9"><path d="M0 0L6 4.5L0 9Z" fill="var(--arrow)"/></svg>Main Course (Curries)</li>
</ul>
<div class="more" style="left:984px;top:548px;background:transparent">More...</div>

<h2 style="left:147px;top:615px;color:var(--accent)">About OLD BRACKLEY</h2>
<p class="about-text">Lorem Ipsum is simply dummy text of the printing and typesetting industry. Lorem Ipsum has been the industry's standard dummy text ever since the 1500s, when an unknown printer took a galley of type and scrambled it to make a type specimen book. It has survived not only five centuries, but also the leap into electronic typesetting, remaining essentially unchanged. It was popularised in the 1960s with the release of Lettersheet sheets containing Lorem Ipsum passages, and more recently with desktop publishing software like Pagecraft Studio including versions of Lorem Ipsum.</p>

<h2 style="left:893px;top:615px">Contact :</h2>
<address class="contact" style="font-style:normal">
  OLD BRACKLEY<br>
  #&nbsp; 2140 Laneway Row<br>
  Lorem Ipsum is simply<br>
  Sydney 97512, Australia.
</address>

<footer class="footer">
  <nav class="footnav">
    <a style="left:401px">Home</a>
    <a style="left:475px">About Us</a>
    <a style="left:568px">Menu</a>
    <a style="left:640px">Events</a>
    <a style="left:718px">Contact Us</a>
  </nav>
  <p class="copy">© 2013 OLD BRACKLEY All Rights Reserved.</p>
</footer>
</body>
</html>
```